Package Design for Toe Warmer Countdown Chest™

Looking to have the 2018 edition of our annual Toe Warmer Countdown Chest™ graphics designed. The packaging is a complex dye the we already have, so positioning and dimensions are not an option.

If you can make the design a 4-color (spot) design, we're open to that, otherwise full CMYK is perfectly acceptable.

Attached are the 2016 & 2017 for reference. You can use the 2017 file as the best option for starting as a template.

Industry/Entity Type

Fashion

Colors

Designer to choose colors to be used in the design.

Requirements
Must have
• The numbers 1 through 24 must stay in the same position, but font can change.
Nice to have
• Pattern/design will match on seem where box is attached.

```html
<!DOCTYPE html>
<html lang="en">
<head>
<meta charset="utf-8">
<title>Toe Warmer Countdown Chest™ – Packaging Panels</title>
<link rel="stylesheet" href="https://fonts.googleapis.com/css2?family=Mountains+of+Christmas:wght@700&family=Hind:wght@400;600&display=swap">
<style>
  :root {
    --red-core: #e8304a;
    --red-mid: #c9213a;
    --red-edge: #9e1627;
    --cream: #f7f0d2;
    --cream-edge: #e6dcb2;
    --ink: #1d1a1a;
    --snow: #ffffff;
    --snow-shade: #f3e4e6;
    --backdrop: #f4eef0;
    --brand-red: #c8233a;
  }
  * { box-sizing: border-box; margin: 0; padding: 0; }
  html, body { width: 1200px; height: 1053px; overflow: hidden; }
  body {
    background: var(--backdrop);
    font-family: "Hind", sans-serif;
    position: relative;
  }
  .panel {
    position: absolute;
    top: 76px;
    width: 540px;
    height: 900px;
    overflow: hidden;
    background: radial-gradient(ellipse at 50% 42%, var(--red-core) 0%, var(--red-mid) 45%, var(--red-edge) 100%);
  }
  .panel--front { left: 40px; }
  .panel--back { left: 620px; }

  .village {
    position: absolute;
    left: 0;
    width: 100%;
    background: linear-gradient(180deg, rgba(255,255,255,0.25) 0%, rgba(255,255,255,0.85) 30%, var(--snow) 55%);
  }
  .panel--front .village { top: 600px; height: 300px; }
  .panel--back .village { top: 560px; height: 340px; }
  .ground {
    position: absolute;
    left: 0; bottom: 0;
    width: 100%;
    background: var(--snow);
  }
  .panel--front .ground { height: 170px; }
  .panel--back .ground { height: 230px; }

  .door-grid {
    position: absolute;
    top: 44px;
    left: 82px;
    display: grid;
    grid-template-columns: repeat(4, 100px);
    grid-auto-rows: 116px;
    gap: 14px 10px;
  }
  .door {
    background: var(--cream);
    border-radius: 8px;
    box-shadow: inset 0 0 0 4px var(--cream), inset 0 0 0 5px var(--cream-edge);
    outline: 1.5px dashed #8f8670;
    outline-offset: -7px;
    display: flex;
    align-items: center;
    justify-content: center;
    font-family: "Mountains of Christmas", cursive;
    font-weight: 700;
    font-size: 62px;
    color: var(--ink);
    line-height: 1;
  }

  .social-handle {
    position: absolute;
    left: 34px;
    bottom: 40px;
    transform-origin: left bottom;
    transform: rotate(-90deg) translate(0, 100%);
    font-size: 17px;
    color: var(--brand-red);
    white-space: nowrap;
  }

  .night-scene {
    position: absolute;
    top: 210px;
    left: 110px;
    width: 320px;
    height: 400px;
    border-radius: 50% 50% 40% 40%;
    background: radial-gradient(ellipse at 50% 40%, rgba(247,240,210,0.85) 0%, rgba(247,240,210,0.45) 40%, rgba(232,48,74,0) 72%);
  }

  .greeting {
    position: absolute;
    left: 36px;
    right: 36px;
    bottom: 66px;
    font-size: 10.5px;
    line-height: 1.45;
    color: var(--ink);
    text-align: center;
  }
  .greeting .hashtag {
    display: block;
    text-align: left;
    margin-top: 4px;
  }
  .brand-name {
    position: absolute;
    right: 34px;
    bottom: 22px;
    font-size: 20px;
    font-weight: 600;
    color: var(--brand-red);
    letter-spacing: 0.5px;
  }
</style>
</head>
<body>

  <section class="panel panel--front" aria-label="Front panel with numbered doors">
    <div class="village" role="img" aria-label="Snowy village rooftops and clouds silhouette"><div class="ground"></div></div>

    <div class="door-grid">
      <div class="door">1</div><div class="door">21</div><div class="door">12</div><div class="door">7</div>
      <div class="door">10</div><div class="door">23</div><div class="door">4</div><div class="door">16</div>
      <div class="door">5</div><div class="door">13</div><div class="door">17</div><div class="door">9</div>
      <div class="door">18</div><div class="door">20</div><div class="door">8</div><div class="door">2</div>
      <div class="door">15</div><div class="door">6</div><div class="door">14</div><div class="door">22</div>
      <div class="door">19</div><div class="door">3</div><div class="door">11</div><div class="door">24</div>
    </div>

    <p class="social-handle">ThreadCrateCA</p>
  </section>

  <section class="panel panel--back" aria-label="Back panel">
    <div class="night-scene" role="img" aria-label="Crescent moon and striped hot air balloon in the night sky"></div>
    <div class="village" role="img" aria-label="Snowy village rooftops and clouds silhouette"><div class="ground"></div></div>

    <p class="greeting">
      This twenty-seventeen collection is our most epic to date; we kind of hope you bought two so you won't have to mediate.<br>
      The Toe Warmer Countdown Chest™ ships across our great nation, while the rest of the world expresses its frustration.<br>
      For the third year in a row it arrives only in Canada, so consider yourself lucky cracking open your sock piñata.<br>
      Filled to the brim with socks of such colours, it's certain you'll feel like a person of large dollars.<br>
      The upcoming year is not far away, and with that we wish you good health, adventure and happiness every day.
      <span class="hashtag">#TWCC18</span>
    </p>

    <p class="brand-name">ThreadCrate</p>
  </section>

</body>
</html>
```